Copperline Groundworks – Website Design Brief

Web Design Brief

We are seeking a web designer to build a modern, responsive website for Copperline Groundworks, a Sydney-based earthworks and excavation company.

2. Project Goal
- Build a professional, easy-to-navigate website that:
- Showcases CGW’s capabilities and past projects
- Attracts residential and commercial developers
- Builds credibility and encourages enquiries

3. Target Audience
- Residential developers and home builders
- Commercial construction firms
- Project managers seeking reliable excavation & plant hire services

4. Services to Highlight
- Bulk Excavation
- Detailed Excavation
- Demolition
- Shoring
- Plant Hire

5. Brand Style & Tone
- Clean, bold, and modern
- Professional with a “we get the job done” attitude
- Colors: Lime Green + Concrete Grey (from logo)
- Fonts: Match the modern, rounded, bold typeface in the logo
- Imagery: Showcase big machines, on-site work, before & after shots

6. Website Pages
Recommended structure:
- Home – Quick intro, project highlights, CTA
- About Us – Team story, mission, safety focus
- Services – Separate sections for each core service
- Projects – Case studies or photo gallery
- Plant Hire – Machines available, specs/photos
- Contact – Form + map + details

7. Assets Provided
- Logo (both long + stacked formats)
- Project photos. More can be provided if required.
- Copy: To be drafted

8. Deliverables
Responsive website (desktop/mobile/tablet)
- SEO-ready structure
- CMS (WordPress) for future edits
- Google Maps integration, job enquiry form

Target Market(s)

Target Audience Residential developers and home builders Commercial construction firms Project managers seeking reliable excavation & plant hire services

Industry/Entity Type

Construction

Number of Pages Required

1 page

Requirements
Must have
• Build a professional, easy-to-navigate website that: Showcases CGW’s capabilities and past projects Attracts residential and commercial developers Builds credibility and encourages enquiries
Nice to have
• All provided in the Description
Should not have

```html
<!DOCTYPE html>
<html lang="en">
<head>
<meta charset="utf-8">
<title>Copperline Groundworks – Earthworks and Excavation</title>
<link href="https://fonts.googleapis.com/css2?family=Poppins:wght@300;400;500;600;700&display=swap" rel="stylesheet">
<style>
:root{
  --lime:#8dc63f;
  --lime-dark:#7ab52f;
  --grey:#8a8a8a;
  --ink:#1d1d1d;
  --text:#555;
  --dark:#141414;
  --white:#fff;
  --star:#9ccc2f;
}
*{margin:0;padding:0;box-sizing:border-box}
html,body{width:1200px;height:4299px;overflow:hidden}
body{font-family:"Poppins",sans-serif;color:var(--ink);background:var(--white);position:relative}
.abs{position:absolute}
.topbar{top:0;left:0;width:1200px;height:35px;background:var(--lime);color:#fff;font-size:11px}
.topbar .social{left:34px;top:10px;display:flex;gap:10px}
.topbar .social span{width:14px;height:14px;border:2px solid #fff;border-radius:50%}
.topbar .contact{right:60px;top:10px;display:flex;gap:40px}
.nav{top:35px;left:0;width:1200px;height:77px;background:#fff}
.brand{left:37px;top:24px;font-size:25px;font-weight:600;color:var(--lime);letter-spacing:1px}
.menu{top:33px;left:0;font-size:14px;font-weight:500;color:var(--ink)}
.menu a{position:absolute;white-space:nowrap;text-decoration:none;color:inherit}
.menu a.active{color:var(--grey);border-bottom:2px solid var(--lime);padding-bottom:3px}
.btn-contact{left:1015px;top:27px;width:125px;height:34px;background:var(--grey);color:#fff;font-size:13px;display:flex;align-items:center;justify-content:center}
.btn{background:var(--lime);color:#fff;font-weight:600;display:flex;align-items:center;justify-content:center;font-size:16px}
.hero{top:112px;left:0;width:1200px;height:660px}
.hero-photo{top:0;left:0;width:1200px;height:631px;background:linear-gradient(180deg,#3c4036 0%,#5b5648 45%,#6b6352 100%);clip-path:polygon(0 0,1200px 0,1200px 539px,600px 631px,0 539px)}
.hero-shade{top:0;left:0;width:1200px;height:631px;background:rgba(0,0,0,.35);clip-path:polygon(0 0,1200px 0,1200px 539px,600px 631px,0 539px)}
.hero h1{top:192px;left:0;width:1200px;text-align:center;color:#fff;font-size:48px;font-weight:600;line-height:54px}
.hero p{top:316px;left:340px;width:520px;text-align:center;color:#fff;font-size:12px;line-height:14px}
.hero .btn{top:392px;left:516px;width:180px;height:42px}
.about-frame{top:890px;left:359px;width:195px;height:220px;background:var(--lime)}
.about-photo{top:901px;left:130px;width:412px;height:384px;background:linear-gradient(135deg,#b9bdc2,#8f8a6e 55%,#6d5f4c)}
.about h2{top:930px;left:624px;font-size:28px;font-weight:600}
.about p{left:616px;width:494px;font-size:12px;line-height:16px;color:var(--text)}
.about .btn{top:1217px;left:624px;width:179px;height:43px}
.services-band{top:1384px;left:0;width:1200px;height:339px;background:linear-gradient(90deg,#8fc548,#97cc52 50%,#8fc548)}
.services h2{top:1460px;left:0;width:1226px;text-align:center;color:#fff;font-size:26px;font-weight:600}
.card{background:#fff;border-radius:10px;box-shadow:0 6px 22px rgba(0,0,0,.1)}
.svc{top:1557px;width:258px;height:349px}
.svc .ph{top:12px;left:15px;width:227px;height:138px;border-radius:4px}
.svc .ico{top:136px;left:30px;width:56px;height:56px;border-radius:50%;background:var(--lime);border:3px solid #fff;display:flex;align-items:center;justify-content:center}
.svc h3{top:210px;left:15px;font-size:16px;font-weight:600}
.svc p{top:236px;left:15px;width:228px;font-size:10px;line-height:13px;color:var(--text)}
.svc .more{top:322px;left:20px;font-size:9px;color:var(--lime);font-weight:500;display:flex;align-items:center;gap:6px}
.svc .more i{width:12px;height:12px;border-radius:50%;background:var(--lime);display:inline-block}
.sec-title{left:0;width:1200px;text-align:center;font-size:26px;font-weight:600}
.underline{left:555px;width:74px;height:3px;background:var(--lime)}
.gal{background:#999}
.cta-band{top:2765px;left:0;width:1200px;height:341px;background:linear-gradient(90deg,#4a4f45,#6d6a4e 50%,#5a5f55)}
.cta-shade{top:2765px;left:0;width:1200px;height:341px;background:rgba(0,0,0,.35)}
.cta h2{top:2874px;left:157px;color:#fff;font-size:28px;font-weight:600}
.cta p{top:2925px;left:157px;width:640px;color:#fff;font-size:14px;line-height:20px}
.cta .btn{top:2917px;left:839px;width:179px;height:42px}
.rev{top:3308px;width:270px;height:284px}
.rev .av{top:16px;left:101px;width:68px;height:68px;border-radius:50%}
.rev h4{top:95px;left:0;width:270px;text-align:center;font-size:18px;font-weight:500}
.rev p{top:133px;left:28px;width:214px;text-align:center;font-size:13px;line-height:18px;color:var(--text)}
.rev .stars{top:228px;left:0;width:270px;text-align:center;color:var(--star);font-size:28px;letter-spacing:4px}
.dot{top:3646px;width:18px;height:18px;border-radius:50%;background:#999}
.footer{top:3760px;left:0;width:1200px;height:539px}
.foot-logo{top:3984px;left:87px;width:140px;height:100px;background:#fff;display:flex;flex-direction:column;justify-content:center;padding-left:12px;color:var(--lime);font-weight:600;font-size:20px;line-height:23px}
.foot-social{top:4114px;left:100px;display:flex;gap:42px}
.foot-social span{width:26px;height:26px;border:2px solid #fff;border-radius:50%}
.footer h5{color:#fff;font-size:18px;font-weight:600}
.links{top:4006px;left:496px;color:#fff;font-size:19px}
.links li{list-style:none;display:flex;align-items:center;gap:10px;height:36px}
.links li i{width:14px;height:14px;border:2px solid var(--lime);border-radius:50%;display:inline-block}
.info{left:838px;color:#fff;font-size:19px;display:flex;align-items:center;gap:16px}
.rule{top:4214px;left:105px;width:1016px;height:1px;background:#555}
.copy{top:4250px;color:#fff;font-size:15px}
</style>
</head>
<body>

<header>
  <div class="abs topbar">
    <div class="abs social"><span></span><span></span><span></span></div>
    <div class="abs contact"><span>✉ info@copperline.example</span><span>☎ (123) 456 7890</span></div>
  </div>
  <nav class="abs nav">
    <div class="abs brand">COPPERLINE GROUNDWORKS</div>
    <div class="abs menu">
      <a class="active" style="left:430px">HOME</a>
      <a style="left:512px">ABOUT</a>
      <a style="left:604px">SERVICES</a>
      <a style="left:716px">PROJECTS</a>
      <a style="left:833px">PLANT HIRE</a>
    </div>
    <div class="abs btn-contact">CONTACT US</div>
  </nav>
</header>

<section class="abs hero">
  <div class="abs hero-photo" role="img" aria-label="Excavator on a levelled dirt site between fences"></div>
  <div class="abs hero-shade"></div>
  <svg class="abs" style="top:560px;left:0" width="1200" height="100" viewBox="0 0 1200 100">
    <polygon points="200,16 600,71 1000,16 600,88" fill="var(--lime)"/>
  </svg>
  <h1 class="abs">EARTHWORKS AND<br>EXCAVATION COMPANY</h1>
  <p class="abs">Lorem ipsum dolor sit amet, consectetur adipiscing elit, sed do eiusmod tempor incididunt ut labore et dolore magna aliqua. Ut enim ad minim veniam, quis nostrud exercitation ullamco laboris nisi ut aliquip ex ea commodo consequat.</p>
  <div class="abs btn">GET A QUOTE</div>
</section>

<section class="about">
  <div class="abs about-frame"></div>
  <div class="abs about-photo" role="img" aria-label="Excavator loading a truck on a demolition site"></div>
  <h2 class="abs">ABOUT US</h2>
  <p class="abs" style="top:1010px">Lorem ipsum dolor sit amet, consectetur adipiscing elit, sed do eiusmod tempor incididunt ut labore et dolore magna aliqua. Ut enim ad minim veniam, quis nostrud exercitation ullamco laboris nisi ut aliquip ex ea commodo consequat. Duis aute irure dolor in reprehenderit in voluptate velit esse cillum dolore eu fugiat nulla pariatur. Excepteur sint occaecat cupidatat non proident, sunt in culpa qui officia deserunt mollit anim id est laborum.</p>
  <p class="abs" style="top:1127px">Lorem ipsum dolor sit amet, consectetur adipiscing elit, sed do eiusmod tempor incididunt ut labore et dolore magna aliqua. Ut enim ad minim veniam, quis nostrud exercitation ullamco laboris nisi ut aliquip ex ea commodo consequat.</p>
  <div class="abs btn">MORE ABOUT US</div>
</section>

<section class="services">
  <div class="abs services-band" role="img" aria-label="Trucks on site under a green tint"></div>
  <h2 class="abs">OUR SERVICES</h2>

  <article class="abs card svc" style="left:142px">
    <div class="abs ph" role="img" aria-label="Excavator bucket tipping soil at sunset" style="background:linear-gradient(180deg,#7fb0d8,#c9a46a 60%,#7a5a3a)"></div>
    <div class="abs ico"><svg width="28" height="28" viewBox="0 0 28 28" fill="none" stroke="#fff" stroke-width="2"><rect x="4" y="16" width="20" height="6" rx="3"/><path d="M8 16V10h8l4 6"/></svg></div>
    <h3 class="abs">Bulk Excavation</h3>
    <p class="abs">Lorem ipsum dolor sit amet, consectetuer adipiscing elit. Aenean commodo ligula eget dolor. Aenean massa. Cum sociis natoque penatibus et magnis dis parturient montes, nascetur ridiculus mus.</p>
    <div class="abs more">READ MORE <i></i></div>
  </article>

  <article class="abs card svc" style="left:476px">
    <div class="abs ph" role="img" aria-label="Close view of an excavator arm and bucket" style="background:linear-gradient(135deg,#c9b04a,#6e6550 55%,#3e3a33)"></div>
    <div class="abs ico"><svg width="28" height="28" viewBox="0 0 28 28" fill="none" stroke="#fff" stroke-width="2"><rect x="4" y="16" width="20" height="6" rx="3"/><path d="M8 16V10h8l4 6"/></svg></div>
    <h3 class="abs" style="left:24px">Demolition</h3>
    <p class="abs">Lorem ipsum dolor sit amet, consectetuer adipiscing elit. Aenean commodo ligula eget dolor. Aenean massa. Cum sociis natoque penatibus et magnis dis parturient montes, nascetur ridiculus mus.</p>
    <div class="abs more">READ MORE <i></i></div>
  </article>

  <article class="abs card svc" style="left:808px">
    <div class="abs ph" role="img" aria-label="Yellow excavator parked on a cleared site" style="background:linear-gradient(180deg,#9cc4e0,#d8c35a 55%,#8a7d68)"></div>
    <div class="abs ico" style="left:30px"><svg width="28" height="28" viewBox="0 0 28 28" fill="none" stroke="#fff" stroke-width="2"><rect x="4" y="16" width="20" height="6" rx="3"/><path d="M8 16V10h8l4 6"/></svg></div>
    <h3 class="abs">Plant Hire</h3>
    <p class="abs">Lorem ipsum dolor sit amet, consectetuer adipiscing elit. Aenean commodo ligula eget dolor. Aenean massa. Cum sociis natoque penatibus et magnis dis parturient montes, nascetur ridiculus mus.</p>
    <div class="abs more">READ MORE <i></i></div>
  </article>
</section>

<section class="gallery">
  <h2 class="abs sec-title" style="top:2002px">WORK GALLERY</h2>
  <div class="abs underline" style="top:2053px"></div>
  <div class="abs gal" style="top:2118px;left:164px;width:278px;height:157px;background:linear-gradient(180deg,#a8adb2,#e6e6e6 60%,#555)" role="img" aria-label="White company ute"></div>
  <div class="abs gal" style="top:2288px;left:164px;width:278px;height:334px;background:linear-gradient(180deg,#5a6a55,#cfd2d4 55%,#444)" role="img" aria-label="White tipper truck"></div>
  <div class="abs gal" style="top:2118px;left:459px;width:277px;height:335px;background:linear-gradient(135deg,#b5b9be,#a89a5a 50%,#6b5b48)" role="img" aria-label="Excavator loading a truck on a demolition site"></div>
  <div class="abs gal" style="top:2465px;left:459px;width:277px;height:157px;background:linear-gradient(180deg,#9aa3ab,#8a5a44 55%,#6b6a5a)" role="img" aria-label="Brick house behind a site fence"></div>
  <div class="abs gal" style="top:2118px;left:758px;width:277px;height:157px;background:linear-gradient(135deg,#b7926a,#8c6a4a)" role="img" aria-label="Excavated footings trench"></div>
  <div class="abs gal" style="top:2288px;left:758px;width:277px;height:334px;background:linear-gradient(135deg,#7a6a56,#4e4a42)" role="img" aria-label="Track marks in levelled soil"></div>
</section>

<section class="cta">
  <div class="abs cta-band" role="img" aria-label="Yellow excavator on an open site"></div>
  <div class="abs cta-shade"></div>
  <h2 class="abs">Ready to Start Your Project?</h2>
  <p class="abs">Whether you need site preparation, excavation, grading, or land clearing, our expert team is here to deliver quality work on time and within budget.</p>
  <div class="abs btn">GET A QUOTE</div>
</section>

<section class="reviews">
  <h2 class="abs sec-title" style="top:3194px">WHAT CLIENT SAY’S</h2>
  <div class="abs underline" style="top:3243px"></div>
  <article class="abs card rev" style="left:122px">
    <div class="abs av" style="background:linear-gradient(180deg,#6fa8e0,#d5e6f5)" role="img" aria-label="Client photo"></div>
    <h4 class="abs">John Doe</h4>
    <p class="abs">Lorem ipsum dolor sit amet, consectetur adipiscing elit, sed do eiusmod tempor incididunt ut labore et dolore magna aliqua.</p>
    <div class="abs stars">★★★★★</div>
  </article>
  <article class="abs card rev" style="left:464px">
    <div class="abs av" style="background:linear-gradient(180deg,#8fb4d8,#a88a6a)" role="img" aria-label="Client photo"></div>
    <h4 class="abs">John Doe</h4>
    <p class="abs">Lorem ipsum dolor sit amet, consectetur adipiscing elit, sed do eiusmod tempor incididunt ut labore et dolore magna aliqua.</p>
    <div class="abs stars">★★★★★</div>
  </article>
  <article class="abs card rev" style="left:808px">
    <div class="abs av" style="background:linear-gradient(180deg,#5a5550,#9a8a78)" role="img" aria-label="Client photo"></div>
    <h4 class="abs">John Doe</h4>
    <p class="abs">Lorem ipsum dolor sit amet, consectetur adipiscing elit, sed do eiusmod tempor incididunt ut labore et dolore magna aliqua.</p>
    <div class="abs stars">★★★★★</div>
  </article>
  <div class="abs dot" style="left:557px"></div>
  <div class="abs dot" style="left:597px;background:var(--lime)"></div>
  <div class="abs dot" style="left:637px"></div>
</section>

<footer class="abs footer" style="top:0;height:4299px;pointer-events:none">
  <svg class="abs" style="top:3760px;left:0" width="1200" height="539" viewBox="0 0 1200 539">
    <polygon points="0,110 600,16 1200,110 1200,539 0,539" fill="var(--dark)"/>
    <polygon points="210,58 600,0 990,58 600,14" fill="var(--lime)"/>
  </svg>
  <div class="abs foot-logo">COPPERLINE<br>GROUND-<br>WORKS</div>
  <div class="abs foot-social"><span></span><span></span><span></span></div>
  <h5 class="abs" style="top:3964px;left:496px">QUICK LINKS</h5>
  <ul class="abs links">
    <li><i></i>Home</li><li><i></i>About</li><li><i></i>Services</li><li><i></i>Projects</li><li><i></i>Contact</li>
  </ul>
  <h5 class="abs" style="top:3958px;left:841px">CONTACT INFO</h5>
  <div class="abs info" style="top:4006px">
    <svg width="28" height="28" viewBox="0 0 24 24" fill="var(--lime)"><path d="M6.6 10.8a15 15 0 0 0 6.6 6.6l2.2-2.2a1 1 0 0 1 1-.25 11.4 11.4 0 0 0 3.6.57 1 1 0 0 1 1 1V20a1 1 0 0 1-1 1A17 17 0 0 1 3 4a1 1 0 0 1 1-1h3.5a1 1 0 0 1 1 1c0 1.25.2 2.45.57 3.57a1 1 0 0 1-.25 1z"/></svg>
    (+61) 2 5550 1836</div>
  <div class="abs info" style="top:4073px">
    <svg width="30" height="24" viewBox="0 0 30 24" fill="var(--lime)"><path d="M1 4h28v18H1z"/><path d="M1 4l14 10L29 4" stroke="var(--dark)" stroke-width="2" fill="none"/></svg>
    support@copperline.example</div>
  <div class="abs info" style="top:4142px">
    <svg width="24" height="32" viewBox="0 0 24 32" fill="var(--lime)"><path d="M12 0a11 11 0 0 0-11 11c0 8 11 21 11 21s11-13 11-21A11 11 0 0 0 12 0zm0 15a4 4 0 1 1 0-8 4 4 0 0 1 0 8z"/></svg>
    14 Quarry Lane, Marrickville</div>
  <div class="abs rule"></div>
  <div class="abs copy" style="left:105px">Copyright © 2025, All Rights Reserved.</div>
  <div class="abs copy" style="left:853px">Privacy Policy | Term &amp; Conditions</div>
</footer>

</body>
</html>
```